Real Estate Team Needs Business Cards

Double sided - Team Member on Front, Team Leader on Back (back side will contain more details).
Colors to use:
Red = R: 233 G: 1 B: 2
Grey = R: 89 G: 89 B: 89
Black= R: 0 B: 0 B: 0
** MAIN FOCUS ** ( separate border, color, design, etc. to really stand out - whatever you think draws the most attention ) on both sides for "Sell for 1%‡" and "Buy & receive up to a 1% rebate‡". Must have fine print **
**Please make both sides stand out and look unique / different
Business card to have round corners (standard size 3.5" x 2").:
Document Trim Size
89 x 51 mm
1050 x 600 pixels
Full Bleed Size
92 x 54 mm
1085 x 635 pixels
Basic example provided. Please redesign as you see best. In your design - Please use the same picture on both sides. Name, address, phone number, email, etc. will be provided to the selected design. QR code on back side only if there is room (not important)

```html
<!DOCTYPE html>
<html lang="en">
<head>
<meta charset="utf-8">
<title>Summit Crest Realty – Business Cards</title>
<link rel="stylesheet" href="https://fonts.googleapis.com/css2?family=Lato:wght@400;700;900&display=swap">
<style>
  :root {
    --red: #e90102;
    --grey: #595959;
    --black: #000000;
    --white: #ffffff;
    --canvas: #ededed;
    --photo-top: #dfe3e8;
    --photo-bottom: #2c3f6b;
  }
  * { margin: 0; padding: 0; box-sizing: border-box; }
  html, body { width: 974px; height: 1200px; overflow: hidden; }
  body {
    position: relative;
    background: var(--canvas);
    font-family: "Lato", Arial, sans-serif;
    color: var(--black);
  }
  .card {
    position: absolute;
    background: var(--white);
    overflow: hidden;
  }
  .card--front { left: 46px; top: 51px; width: 883px; height: 518px; }
  .card--back  { left: 50px; top: 644px; width: 876px; height: 513px; }

  .abs { position: absolute; white-space: nowrap; }
  .center { transform: translateX(-50%); }

  .rule { position: absolute; }
  .rule--red { background: var(--red); height: 4px; }
  .rule--black { background: var(--black); height: 3px; }

  .brand-mark {
    display: flex;
    align-items: center;
    gap: 14px;
  }
  .brand-mark__square {
    width: 34px; height: 34px;
    background: var(--red);
  }
  .brand-name {
    font-weight: 900;
    font-size: 46px;
    line-height: 1;
    letter-spacing: 0.5px;
    color: var(--black);
  }
  .card--back .brand-mark__square { width: 30px; height: 30px; }
  .card--back .brand-name { font-size: 40px; }

  .brand-sub {
    display: flex;
    align-items: center;
    gap: 10px;
    font-weight: 700;
    font-size: 12px;
    line-height: 1;
    letter-spacing: 0.5px;
    color: var(--grey);
  }
  .brand-sub::before, .brand-sub::after {
    content: "";
    height: 2px;
    background: var(--red);
  }
  .card--front .brand-sub::before, .card--front .brand-sub::after { width: 160px; }
  .card--back .brand-sub::before, .card--back .brand-sub::after { width: 150px; }

  .offer {
    font-weight: 700;
    color: var(--red);
    line-height: 1;
    font-size: 27px;
  }
  .person-name { font-weight: 700; font-size: 29px; line-height: 1; }
  .person-role { font-weight: 400; font-size: 21px; line-height: 1; color: var(--grey); }
  .contact-label { font-weight: 700; font-size: 20px; line-height: 1; color: var(--red); }
  .team-title { font-weight: 700; font-size: 34px; line-height: 1; }
  .perk { font-weight: 700; font-size: 21px; line-height: 1; color: var(--black); }
  .perk--offer { color: var(--red); }

  .photo {
    position: absolute;
    background: linear-gradient(180deg, var(--photo-top) 0%, var(--photo-top) 35%, var(--photo-bottom) 60%, var(--photo-bottom) 100%);
  }

  .footer-line { position: absolute; right: 0; height: 4px; background: var(--black); }
  .footer-band {
    position: absolute; right: 0; bottom: 0;
    background: var(--red);
  }
  .website {
    font-weight: 400; font-size: 21px; line-height: 1; color: var(--white);
  }
</style>
</head>
<body>

<section class="card card--front" aria-label="Business card front – team member">
  <div class="abs center brand-mark" style="left:444px; top:56px;">
    <span class="brand-mark__square"></span>
    <span class="brand-name">SUMMIT CREST REALTY</span>
  </div>

  <div class="rule rule--red" style="left:0; right:0; top:122px;"></div>
  <div class="rule rule--black" style="left:0; right:0; top:131px;"></div>

  <div class="abs center brand-sub" style="left:444px; top:158px;">INC., BROKERAGE</div>

  <p class="abs center offer" style="left:444px; top:194px;">Sell For 1%</p>
  <p class="abs center offer" style="left:444px; top:226px;">Buy &amp; receive up to a 1% rebate</p>

  <div class="photo" role="img" aria-label="Portrait photo of the team member in a navy suit" style="left:0; top:244px; width:227px; height:274px;"></div>

  <h2 class="abs person-name" style="left:301px; top:292px;">EMPLOYEE NAME</h2>
  <p class="abs person-role" style="left:399px; top:326px;">Position</p>

  <p class="abs contact-label" style="left:300px; top:368px;">Cell:</p>
  <p class="abs contact-label" style="left:300px; top:395px;">Office:</p>
  <p class="abs contact-label" style="left:300px; top:422px;">E-mail:</p>

  <div class="footer-line" style="left:227px; top:456px;"></div>
  <div class="footer-band" style="left:227px; height:51px;"></div>
  <p class="abs center website" style="left:547px; top:482px;">www.website.com</p>
</section>

<section class="card card--back" aria-label="Business card back – team leader">
  <h1 class="abs center team-title" style="left:423px; top:52px;">Summit Crest Real Estate Team</h1>

  <p class="abs contact-label" style="left:46px; top:112px;">Address:</p>
  <p class="abs contact-label" style="left:46px; top:139px;">Office:</p>
  <p class="abs contact-label" style="left:46px; top:166px;">E-mail:</p>

  <div class="abs center brand-mark" style="left:606px; top:126px;">
    <span class="brand-mark__square"></span>
    <span class="brand-name">SUMMIT CREST REALTY</span>
  </div>

  <div class="rule rule--red" style="left:384px; width:445px; top:180px;"></div>
  <div class="rule rule--black" style="left:384px; width:445px; top:189px;"></div>

  <div class="abs center brand-sub" style="left:606px; top:206px;">INC., BROKERAGE</div>

  <p class="abs perk perk--offer" style="left:384px; top:246px;">Sell For 1%</p>
  <p class="abs perk perk--offer" style="left:384px; top:273px;">Buy &amp; receive up to a 1% rebate</p>
  <p class="abs perk" style="left:384px; top:300px;">Free home evaluation</p>
  <p class="abs perk" style="left:384px; top:327px;">Free local sold reports</p>
  <p class="abs perk" style="left:384px; top:354px;">Advanced Propery Search</p>

  <div class="photo" role="img" aria-label="Portrait photo of the team leader in a navy suit" style="left:0; top:245px; width:224px; height:268px;"></div>

  <h2 class="abs person-name" style="left:244px; top:388px;">OWNER NAME</h2>
  <p class="abs person-role" style="left:369px; top:421px;">Position</p>

  <div class="footer-line" style="left:224px; top:452px;"></div>
  <div class="footer-band" style="left:224px; height:50px;"></div>
  <p class="abs center website" style="left:544px; top:478px;">www.website.com</p>
</section>

</body>
</html>
```